Female Leadership Word/PDF template

I need a template, not just a design, for a word document in A4 size with a cover, middle pages and last page to give a nice as course material for a leadership training. I need it as a document to directly work in myself, to put in the text etc, ready to use , not just the design. I have attached 3 files. One that is an inspiration for how I like to have it (except the photos), one that is my style guide that shows the different elements to play with. I like it to be bright and stylish at the same time. I've added another document that shows some bright colors. My web page is www.brightmeadow.se

Target Market(s)

Women leaders who like to perform but want to increase the soft and spiritual side in their lives and profession.

Industry/Entity Type

Leadership

Font styles to use
Sans Serif

Colors

Designer to choose colors to be used in the design.

Requirements
Must have
• Feel elegant, warm, welcoming and professional.
• Must be a document I can work in, not just a design that I should apply. Willing to pay more for that.
Should not have
• Dull. Hard.

```html
<!DOCTYPE html>
<html lang="en">
<head>
<meta charset="utf-8">
<title>Bright Meadow – Course Material Template</title>
<link href="https://fonts.googleapis.com/css2?family=Montserrat:wght@300;400;600;700;800&display=swap" rel="stylesheet">
<style>
  :root {
    --orange: #ef7d22;
    --orange-light: #f4a13f;
    --orange-header: #f0a04b;
    --sand: #a39478;
    --paper: #ffffff;
    --ink: #6b6b6b;
    --panel-grey: #ececec;
    --backdrop: #ffffff;
  }
  * { margin: 0; padding: 0; box-sizing: border-box; }
  html, body {
    width: 1200px; height: 866px; overflow: hidden;
    background: var(--backdrop);
    font-family: 'Montserrat', Arial, sans-serif;
  }
  .spread { position: relative; width: 1200px; height: 866px; }

  .page {
    position: absolute; top: 13px; width: 572px; height: 843px;
    background: var(--paper); overflow: hidden;
    border: 1px solid #d9d9d9;
  }
  .page--cover { left: 14px; }
  .page--inner { left: 612px; }

  /* Cover */
  .cover-visual {
    position: absolute; left: 0; top: 0; width: 100%; height: 645px;
    background:
      radial-gradient(ellipse at 30% 55%, rgba(255,190,110,.45), transparent 55%),
      radial-gradient(ellipse at 85% 20%, rgba(230,100,20,.55), transparent 50%),
      linear-gradient(160deg, #f29a38 0%, #f08a2a 45%, #ee7d22 100%);
  }
  .cover-title {
    position: absolute; left: 0; right: 0; top: 330px;
    text-align: center; color: #fff;
  }
  .cover-title__name { font-weight: 300; font-size: 30px; letter-spacing: 1.5px; line-height: 38px; }
  .cover-title__date { font-weight: 700; font-size: 30px; letter-spacing: 1px; line-height: 40px; }
  .cover-band {
    position: absolute; left: 0; bottom: 0; width: 100%; height: 198px;
    background: var(--sand);
  }
  .brand { position: absolute; display: flex; align-items: center; color: #fff; }
  .brand__dot { border-radius: 50%; border: 2px solid #fff; }
  .brand--cover { left: 140px; top: 68px; }
  .brand--cover .brand__dot { width: 68px; height: 68px; margin-right: 16px; }
  .brand--cover .brand__name { font-size: 36px; font-weight: 400; letter-spacing: -.5px; }

  /* Inner page */
  .inner-header {
    position: absolute; left: 0; top: 0; width: 100%; height: 53px;
    background: var(--orange-header);
  }
  .inner-header__title {
    position: absolute; left: 19px; top: 13px;
    color: #fff; font-size: 22px; font-weight: 800; letter-spacing: .8px;
  }
  .brand--header { right: 14px; top: 11px; }
  .brand--header .brand__dot { width: 30px; height: 30px; margin-right: 8px; }
  .brand--header .brand__name { font-size: 18px; font-weight: 400; }

  .side-panel {
    position: absolute; left: 156px; top: 53px; right: 0; bottom: 26px;
    background: linear-gradient(90deg, #fafafa 0%, #f3f3f3 60%, var(--panel-grey) 100%);
  }
  .side-ornament {
    position: absolute; left: -200px; top: 110px; width: 360px; height: 640px;
    border-radius: 50%;
    background: radial-gradient(circle at 60% 50%, rgba(225,220,210,.55), rgba(225,220,210,.15) 60%, transparent 72%);
  }

  .content { position: absolute; left: 45px; top: 88px; width: 508px; color: var(--ink); }
  .content p {
    font-size: 11.6px; line-height: 20.1px; overflow: hidden; word-spacing: .5px;
  }
  .content .para-1 { height: 241px; }
  .content .para-2 { height: 181px; }
  .content .para-3 { height: 141px; margin-top: 20px; }
  .content h2 {
    color: var(--orange); font-size: 16.5px; font-weight: 700;
    line-height: 20px; margin: 10px 0 1px;
  }

  .inner-footer {
    position: absolute; left: 0; bottom: 0; width: 100%; height: 26px;
    background: var(--sand);
  }
  .inner-footer__copy {
    position: absolute; left: 10px; top: 7px;
    color: #fff; font-size: 10.5px; letter-spacing: .6px;
  }
  .inner-footer__page {
    position: absolute; right: 0; top: 0; height: 26px; width: 92px;
    background: var(--orange-light);
    clip-path: polygon(18% 0, 100% 0, 100% 100%, 0 100%);
    color: #fff; font-size: 10.5px; letter-spacing: .6px;
    padding: 7px 10px 0 0; text-align: right;
  }
</style>
</head>
<body>
<main class="spread">

  <section class="page page--cover">
    <div class="cover-visual" role="img" aria-label="Warm orange photograph of meadow grass in soft sunlight"></div>
    <div class="cover-title">
      <div class="cover-title__name">DOCUMENT TITLE HERE</div>
      <div class="cover-title__date">MARCH 2019</div>
    </div>
    <div class="cover-band">
      <div class="brand brand--cover">
        <span class="brand__dot"></span>
        <span class="brand__name">Bright Meadow</span>
      </div>
    </div>
  </section>

  <section class="page page--inner">
    <div class="side-panel"></div>
    <div class="side-ornament" role="img" aria-label="Faint circular decorative pattern"></div>

    <header class="inner-header">
      <h1 class="inner-header__title">EXECUTIVE SUMMARY</h1>
      <div class="brand brand--header">
        <span class="brand__dot"></span>
        <span class="brand__name">Bright Meadow</span>
      </div>
    </header>

    <article class="content">
      <p class="para-1">Lorem ipsum dolor sir Lorem ipsum dolor sirLorem ipsum dolor sirLorem ipsum dolor sirLorem ipsum dolor sirLorem ipsum dolor sirLorem ipsum dolor sirLorem ipsum dolor sirLorem ipsum dolor sir Lorem ipsum dolor sirLorem ipsum dolor sirLorem ipsum dolor sirLorem ipsum dolor sirLorem ipsum dolor sirLorem ipsum dolor sirLorem ipsum dolor sirLorem ipsum dolor sir Lorem ipsum dolor sirLorem ipsum dolor sirLorem ipsum dolor sirLorem ipsum dolor sirLorem ipsum dolor sirLorem ipsum dolor sirLorem ipsum dolor sirLorem ipsum dolor sir Lorem ipsum dolor sirLorem ipsum dolor sirLorem ipsum dolor sirLorem ipsum dolor sirLorem ipsum dolor sirLorem ipsum dolor sirLorem ipsum dolor sirLorem ipsum dolor sir Lorem ipsum dolor sirLorem ipsum dolor sirLorem ipsum dolor sirLorem ipsum dolor sirLorem ipsum dolor sirLorem ipsum dolor sirLorem ipsum dolor sirLorem ipsum dolor sir Lorem ipsum dolor sirLorem ipsum dolor sirLorem ipsum dolor sirLorem ipsum dolor sirLorem ipsum dolor</p>

      <h2>Paragaraph Title here</h2>
      <p class="para-2">sirLorem ipsum dolor sirLorem ipsum dolor sirLorem ipsum dolor sir Lorem ipsum dolor sirLorem ipsum dolor sirLorem ipsum dolor sirLorem ipsum dolor sirLorem ipsum dolor sirLorem ipsum dolor sirLorem ipsum dolor sirLorem ipsum dolor sir Lorem ipsum dolor sirLorem ipsum dolor sirLorem ipsum dolor sirLorem ipsum dolor sirLorem ipsum dolor sirLorem ipsum dolor sirLorem ipsum dolor sirLorem ipsum dolor sir Lorem ipsum dolor sirLorem ipsum dolor sirLorem ipsum dolor sirLorem ipsum dolor sirLorem ipsum dolor sirLorem ipsum dolor sirLorem ipsum dolor sirLorem ipsum dolor sir Lorem ipsum dolor sirLorem ipsum dolor sirLorem ipsum dolor sirLorem ipsum dolor sirLorem ipsum dolor sirLorem ipsum dolor sirLorem ipsum dolor sir</p>

      <p class="para-3">sirLorem ipsum dolor sirLorem ipsum dolor sirLorem ipsum dolor sir Lorem ipsum dolor sirLorem ipsum dolor sirLorem ipsum dolor sirLorem ipsum dolor sirLorem ipsum dolor sirLorem ipsum dolor sirLorem ipsum dolor sirLorem ipsum dolor sir Lorem ipsum dolor sirLorem ipsum dolor sirLorem ipsum dolor sirLorem ipsum dolor sirLorem ipsum dolor sirLorem ipsum dolor sirLorem ipsum dolor sirLorem ipsum dolor sir Lorem ipsum dolor sirLorem ipsum dolor sirLorem ipsum dolor sirLorem ipsum dolor sirLorem ipsum dolor sirLorem ipsum dolor sirLorem ipsum dolor sir</p>
    </article>

    <footer class="inner-footer">
      <span class="inner-footer__copy">COPYRIGHT TEXT HERE</span>
      <span class="inner-footer__page">PAGE : 06</span>
    </footer>
  </section>

</main>
</body>
</html>
```